DUXOVE Flyer

We would like the option of being able to fill in a text box so we would need an editable file to type in our information.
You can add wording to it yourself where you see fit
We would like better designs than the ones we are sending as well.
We would like the lumo grove logo add on the flyer. We want the exact logo but not the back ground. We would like the logo to show up multiple times if possible.
You are free to be creative with the design. If you have ideas that are not listed in the description, feel free to design them.
Thanks!!!
Family Insurance

```html
<!DOCTYPE html>
<html lang="en">
<head>
<meta charset="utf-8">
<title>Lumo Grove – Family Insurance Flyer</title>
<link rel="stylesheet" href="https://fonts.googleapis.com/css2?family=Barlow:wght@700;800&family=Noto+Sans:wght@400&display=swap">
<style>
  :root {
    --brand-red: #e31d2b;
    --frame-red: #d9333c;
    --shadow-ink: #1c1c1c;
    --body-ink: #1e1e1e;
    --paper: #ffffff;
    --paper-top: #ececec;
    --suit-light: #b9c3cf;
    --suit-dark: #7f8a98;
  }
  * { margin: 0; padding: 0; box-sizing: border-box; }
  html, body { width: 816px; height: 1200px; overflow: hidden; background: var(--paper); }
  .flyer {
    position: relative;
    width: 816px;
    height: 1200px;
    background: linear-gradient(to bottom, var(--paper-top) 0, var(--paper) 260px, var(--paper) 100%);
    overflow: hidden;
  }
  .flyer__frame {
    position: absolute;
    left: 16px; top: 19px;
    width: 782px; height: 1162px;
    border: 1.5px solid var(--frame-red);
  }
  .headline {
    position: absolute;
    left: 53px; top: 50px;
    font-family: "Barlow", "Arial Narrow", sans-serif;
    font-weight: 800;
    font-size: 80px;
    line-height: 94px;
    letter-spacing: 1px;
    color: var(--brand-red);
    text-shadow: 4px 4px 0 var(--shadow-ink);
    text-transform: uppercase;
    white-space: nowrap;
  }
  .copy {
    position: absolute;
    font-family: "Noto Sans", "Helvetica Neue", sans-serif;
    font-size: 15.5px;
    line-height: 22px;
    letter-spacing: 0.5px;
    color: var(--body-ink);
    white-space: nowrap;
  }
  .copy p + p { margin-top: 22px; }
  .copy .line { display: block; }
  .copy--intro { left: 56px; top: 287px; }
  .copy--offer { left: 425px; top: 382px; }
  .brand-mark {
    position: absolute;
    left: 58px; top: 900px;
    display: flex;
    align-items: center;
    gap: 10px;
    font-family: "Barlow", "Arial Narrow", sans-serif;
    font-weight: 700;
    font-size: 40px;
    line-height: 44px;
    color: var(--brand-red);
  }
  .brand-mark__dot {
    width: 28px; height: 28px;
    border-radius: 50%;
    background: var(--brand-red);
  }
  .agent-portrait {
    position: absolute;
    left: 328px; top: 650px;
    width: 452px; height: 531px;
  }
</style>
</head>
<body>
  <main class="flyer">
    <div class="flyer__frame"></div>

    <h1 class="headline">Your Family It’s<br>Our Concerns</h1>

    <section class="copy copy--intro">
      <p>
        <span class="line">YOUR FAMILY’S CONCERNS are, no</span>
        <span class="line">doubt, of utmost importance to you.</span>
        <span class="line">After all, what’s more important than</span>
        <span class="line">the well-being of those you love? When</span>
        <span class="line">a medical emergency arises, you con-</span>
        <span class="line">sult a specialist. When you face a legal</span>
        <span class="line">issue, you turn to a trusted profes-</span>
        <span class="line">sional with the experience and skill to</span>
        <span class="line">handle your needs. It’s the same when</span>
        <span class="line">it comes to insurance.</span>
      </p>
      <p>
        <span class="line">HAVING the proper insurance program</span>
        <span class="line">is one of the most important steps your</span>
        <span class="line">family can take. Why trust those crucial</span>
        <span class="line">decisions to chance? The time to</span>
        <span class="line">choose the right insurance professional</span>
        <span class="line">is before you need one. That’s where</span>
        <span class="line">Marcus Hale can help. He is one of</span>
        <span class="line">Tulsa’s leading agents. Helping families</span>
        <span class="line">like yours isn’t just his job, it’s his</span>
        <span class="line">commitment. Before you renew your</span>
        <span class="line">next insurance premium, don’t you owe</span>
        <span class="line">it to yourself—and your family—to at</span>
        <span class="line">least find out how his unique brand of</span>
        <span class="line">personal service and extraordinary</span>
        <span class="line">results can make a difference?</span>
      </p>
    </section>

    <section class="copy copy--offer">
      <p>
        <span class="line">CALL FOR YOUR COPY of LUMO grove</span>
        <span class="line">free special report, “How to Select a</span>
        <span class="line">Personal Insurance Agent and Why</span>
        <span class="line">Having One is Important to Your</span>
        <span class="line">Future.” Whether or not you decide to</span>
        <span class="line">work with us, he simply wants to make</span>
        <span class="line">sure your insurance experience is the</span>
        <span class="line">kind of service you deserve—the very</span>
        <span class="line">best. Call us today. You’ll be glad you</span>
        <span class="line">did.</span>
      </p>
    </section>

    <div class="brand-mark">
      <span class="brand-mark__dot"></span>
      <span class="brand-mark__name">Lumo Grove</span>
    </div>

    <svg class="agent-portrait" viewBox="0 0 452 531" role="img" aria-label="Portrait photo of the insurance agent in a light grey suit and navy tie, arms crossed">
      <defs>
        <linearGradient id="suitTone" x1="0" y1="0" x2="0" y2="1">
          <stop offset="0" stop-color="#b9c3cf"/>
          <stop offset="0.55" stop-color="#a6b1bf"/>
          <stop offset="1" stop-color="#7f8a98"/>
        </linearGradient>
      </defs>
      <path fill="url(#suitTone)" d="M136 531 L136 531 L0 531 L10 300 Q20 240 90 225 L150 200 Q136 150 136 90 Q136 0 216 0 Q296 0 296 90 Q296 150 282 200 L360 230 Q430 250 440 320 L452 531 Z"/>
    </svg>
  </main>
</body>
</html>
```